A5 Flyer for Financial Services Business

I am after a re-design of our business flyer to fit in with our new branding style and logo colour scheme. Wanting something with a bit of designer flair that I could not create myself. I have included the flyer which I created which lacks style so dazzle me.

I want to use the same content.

Text for main body of flyer is

Are you a small business owner, tradie or KTAV Service Provider struggling to stay on top of your bookkeeping and compliance obligations? If so we would love to help you get back on track and take control of your business finances so that you can make informed business decisions and focus on what you do best.

We have over 20 years industry experience and, as a small business ourselves, we are able to offer our clients a personal bookkeeping solution tailored to meet the needs of your business.

Accounts Payable | Accounts Receivable
Customer Invoicing
Bank and Credit Card Reconciliations
Payroll | Superannuation | Payroll Tax
Business Activity | Instalment Activity Statements
Regular Financial Reports
Ledgra and Tallybook Set-Up and Training

```html
<!DOCTYPE html>
<html lang="en">
<head>
<meta charset="utf-8">
<title>Even Ledger Financial Services – Bookkeeping Flyer</title>
<link href="https://fonts.googleapis.com/css2?family=Open+Sans:wght@700&family=Source+Sans+3:wght@400&family=Ubuntu:wght@500&family=Roboto+Condensed:wght@500&display=swap" rel="stylesheet">
<style>
  :root{
    --teal:#0f8b96;
    --teal-dark:#0b737d;
    --teal-text:#148a9b;
    --navy:#23338f;
    --blue:#1460ae;
    --paper:#eef5fb;
    --ink:#1d1d1f;
    --grey:#8f9296;
    --badge:#dfe4e8;
    --footer-ink:#163c44;
    --white:#ffffff;
  }
  *{margin:0;padding:0;box-sizing:border-box}
  html,body{width:846px;height:1200px;overflow:hidden;background:var(--white)}
  .flyer{position:relative;width:846px;height:1200px;background:var(--paper);overflow:hidden;font-family:"Source Sans 3",sans-serif}
  .masthead{position:absolute;left:0;top:0;width:846px;height:163px;background:var(--white)}
  .brand{position:absolute;left:0;width:846px;top:74px;text-align:center;color:var(--teal-dark);font-family:"Roboto Condensed",sans-serif;font-weight:500}
  .brand-name{font-size:31px;letter-spacing:-0.5px;line-height:32px;text-transform:uppercase}
  .brand-sub{font-size:14px;letter-spacing:7px;line-height:18px}
  .brand-mark{display:inline-block;width:14px;height:14px;background:var(--teal-dark);margin-right:8px;vertical-align:2px}
  .hero-photo{position:absolute;left:2px;top:163px;width:844px;height:464px;background:linear-gradient(120deg,#dfe6ee 0%,#c9b49a 35%,#d79a3a 50%,#3a3e4a 68%,#d8c3b3 85%,#2c3550 100%)}
  .banner{position:absolute;left:18px;top:135px;width:787px;height:56px;background:linear-gradient(90deg,var(--navy),var(--blue));color:var(--white);font-family:"Open Sans",sans-serif;font-weight:700;font-size:21px;letter-spacing:2.3px;text-align:center;line-height:56px}
  .intro{position:absolute;left:57px;top:651px;width:733px;font-size:20.2px;line-height:24.3px;color:var(--ink);text-align:justify;text-align-last:left}
  .intro p+p{margin-top:24px}
  .teal-base{position:absolute;left:0;top:0}
  .services-card{position:absolute;left:45px;top:861px;width:756px;height:243px;background:var(--white);border:4px solid var(--teal);border-radius:32px}
  .badge{position:absolute;left:22px;top:26px;width:84px;height:84px;border-radius:14px;background:var(--badge)}
  .agent{position:absolute;left:20px;top:128px;width:90px;text-align:center;font-family:Arial,sans-serif;font-size:9.5px;line-height:13px;color:#333}
  .services{position:absolute;left:142px;top:14px;list-style:none;font-family:"Ubuntu",sans-serif;font-weight:500;font-size:19px;color:var(--teal-text)}
  .services li{height:24.1px;line-height:24px;display:flex;align-items:center}
  .services svg{width:17px;height:17px;margin-right:20px;flex:none}
  .accreditations{position:absolute;top:202px;left:0;width:100%;font-family:"Ubuntu",sans-serif;font-weight:500;font-size:19px;color:var(--ink)}
  .accreditations span{position:absolute;display:flex;align-items:center;white-space:nowrap}
  .diamond{width:15px;height:15px;transform:rotate(45deg);margin-right:28px}
  .contact{position:absolute;top:1128px;font-family:"Ubuntu",sans-serif;font-weight:500;font-size:17px}
  .contact-row{display:flex;align-items:center;height:30px;white-space:nowrap}
  .contact svg{width:22px;height:22px;margin-right:8px;flex:none}
  .address{left:21px;color:var(--footer-ink)}
  .address .indent{padding-left:30px}
  .web{left:251px;color:var(--white)}
  .phone{left:659px;color:var(--white)}
  .phone svg{margin-right:16px}
  .divider{position:absolute;top:1130px;width:2px;height:52px;background:var(--white)}
</style>
</head>
<body>
<div class="flyer">
  <header class="masthead">
    <div class="brand">
      <div class="brand-name"><span class="brand-mark"></span>Even Ledger</div>
      <div class="brand-sub">Financial Services</div>
    </div>
  </header>

  <div class="hero-photo" role="img" aria-label="Four smiling women gathered around a laptop in a bright office"></div>
  <h1 class="banner">Bookkeeping Tailored to Your Business Needs</h1>

  <section class="intro">
    <p>Are you a small business owner, tradie or KTAV Service Provider struggling to stay on top of your bookkeeping and compliance obligations? If so we would love to help you get back on track and take control of your business finances so that you can make informed business decisions and focus on what you do best.</p>
    <p>We have over 20 years industry experience and, as a small business ourselves, we are able to offer our clients a personal bookkeeping solution tailored to meet the needs of your business.</p>
  </section>

  <svg class="teal-base" width="846" height="1200" viewBox="0 0 846 1200" aria-hidden="true">
    <path d="M0 1022 L48 982 L798 982 L846 1022 L846 1200 L0 1200 Z" fill="var(--teal)"/>
    <path d="M0 1060 L48 1020 L48 1200 L0 1200 Z M846 1060 L798 1020 L798 1200 L846 1200 Z" fill="var(--teal-dark)" opacity="0.35"/>
  </svg>

  <section class="services-card">
    <div class="badge" role="img" aria-label="Registered agent badge"></div>
    <div class="agent">BAS agent<br>40718263</div>
    <ul class="services">
      <li><svg viewBox="0 0 20 20"><circle cx="10" cy="10" r="10" fill="var(--teal)"/><path d="M5.5 10.5l3 3 6-6.5" stroke="#fff" stroke-width="2.2" fill="none"/></svg>Accounts Payable | Accounts Receivable</li>
      <li><svg viewBox="0 0 20 20"><circle cx="10" cy="10" r="10" fill="var(--teal)"/><path d="M5.5 10.5l3 3 6-6.5" stroke="#fff" stroke-width="2.2" fill="none"/></svg>Customer Invoicing</li>
      <li><svg viewBox="0 0 20 20"><circle cx="10" cy="10" r="10" fill="var(--teal)"/><path d="M5.5 10.5l3 3 6-6.5" stroke="#fff" stroke-width="2.2" fill="none"/></svg>Bank and Credit Card Reconciliations</li>
      <li><svg viewBox="0 0 20 20"><circle cx="10" cy="10" r="10" fill="var(--teal)"/><path d="M5.5 10.5l3 3 6-6.5" stroke="#fff" stroke-width="2.2" fill="none"/></svg>Payroll | Superannuation | Payroll Tax</li>
      <li><svg viewBox="0 0 20 20"><circle cx="10" cy="10" r="10" fill="var(--teal)"/><path d="M5.5 10.5l3 3 6-6.5" stroke="#fff" stroke-width="2.2" fill="none"/></svg>Regular Financial Reports</li>
      <li><svg viewBox="0 0 20 20"><circle cx="10" cy="10" r="10" fill="var(--teal)"/><path d="M5.5 10.5l3 3 6-6.5" stroke="#fff" stroke-width="2.2" fill="none"/></svg>Business Activity | Instalment Activity Statements</li>
      <li><svg viewBox="0 0 20 20"><circle cx="10" cy="10" r="10" fill="var(--teal)"/><path d="M5.5 10.5l3 3 6-6.5" stroke="#fff" stroke-width="2.2" fill="none"/></svg>Ledgra and Tallybook Set-Up and Training</li>
    </ul>
    <div class="accreditations">
      <span style="left:87px"><i class="diamond" style="background:var(--grey)"></i>Ledgra Certified Advisor</span>
      <span style="left:418px"><i class="diamond" style="background:var(--teal)"></i>Tallybook Pro Advisor</span>
    </div>
  </section>

  <div class="contact address">
    <div class="contact-row"><svg viewBox="0 0 24 24"><circle cx="12" cy="12" r="11" fill="none" stroke="var(--footer-ink)" stroke-width="1.3"/><path d="M12 5.5a4.2 4.2 0 0 0-4.2 4.2c0 3.2 4.2 8 4.2 8s4.2-4.8 4.2-8A4.2 4.2 0 0 0 12 5.5z" fill="var(--white)"/><circle cx="12" cy="9.7" r="1.6" fill="var(--teal)"/></svg>PO Box 482</div>
    <div class="contact-row indent" style="margin-top:2px">Kelvale NSW 2391</div>
  </div>
  <div class="divider" style="left:216px"></div>
  <div class="contact web">
    <div class="contact-row"><svg viewBox="0 0 24 24"><circle cx="12" cy="12" r="11" fill="none" stroke="var(--footer-ink)" stroke-width="1.3"/><path d="M6.5 10.5L12 6.5l5.5 4v7h-11z" fill="var(--white)"/><path d="M6.5 10.5L12 14l5.5-3.5" stroke="var(--teal)" fill="none"/></svg>info@evenledgerfinancial.com.au</div>
    <div class="contact-row" style="margin-top:2px"><svg viewBox="0 0 24 24"><circle cx="12" cy="12" r="11" fill="none" stroke="var(--footer-ink)" stroke-width="1.3"/><circle cx="12" cy="12" r="6.5" fill="var(--white)"/><path d="M5.5 12h13M12 5.5v13M8 8.5h8M8 15.5h8" stroke="var(--teal)" stroke-width="0.9"/></svg>www.evenledgerfinancial.com.au</div>
  </div>
  <div class="divider" style="left:645px"></div>
  <div class="contact phone">
    <div class="contact-row"><svg viewBox="0 0 24 24"><circle cx="12" cy="12" r="11" fill="none" stroke="var(--footer-ink)" stroke-width="1.3"/><path d="M8.2 6.5l2 2.4-1.1 1.5c.8 1.7 2 2.9 3.6 3.7l1.5-1.1 2.4 2-1.2 1.9C11 16.5 7.5 13 6.6 8z" fill="var(--white)"/></svg>0400 555 018</div>
  </div>
</div>
</body>
</html>
```